"Het Zaakkompas" needs a new Web Design

We need a web design for to support the startup of a new Activity.

Het Zaakkompas is a company that offers consulting services towards SMB based in Belgium. Focus of the consultancy is:
-Marketing
-Sales
-ICT

We would like to see designs that use the color blue and that fit's with our logo.

The website should communicate trust and expertise.

Main goal of the website is to attract new professional customers

We think of providing following content on the site:
-Home Page
-Who we are (present our 3 team members)
-How we work
-Skills we offer
-Contact us
-Groeiateliers (Free workshops we offer on a regular base)
-Blog

In a later stage:
-Testimonials
-Create & Integrate an animation where we present our services

Call To Actions:
-Register for our newsletter
-Register for a Groeiatelier
-Ask a free intake meeting

CTA's will change from time to time.
Design has to be responsive

Site will be made in wordpress. Design should fit in a existing template so we do not have to start from scratch.

see www.zaakkompas.be

The logo attached is just new. Feel free if yoy have any suggestions to approve this!

Target Market(s)

SMB companies that likes to grow and and expand there business

Industry/Entity Type

Management Consulting

Contact Information for Business Card

I was thinking of including there a picture in from ourselves

Coding

Coded - Design and coding required

Number of Pages Required

5+ page

Font styles to use
Sans Serif

Colors
3277b5
0592cd
33a6d7
85cae6
85acd2
fcfafc

Requirements
Must have
• I'm using the themes from Velvet Layouts
• For example Orla. Should nice tu use this.
• http://www.velvetlayouts.com/gallery/orla/
• I like the design from this site.
• http://www.ondernemershulp-veldhoek.be/#home
• Header menu can better but the thing I realy like is the design of the "Missie" page. the "animation"
Should not have
• I do not want a traditional design.
• Other sites I like:
• https://www.mailpeloton.com/
• https://www.staylantern.com
• https://www.tallygrove.com
• http://www.voxtrellis.com
• http://www.craftbazaru.com/

```html
<!DOCTYPE html>
<html lang="en">
<head>
<meta charset="utf-8">
<title>Het Zaakkompas</title>
<link href="https://fonts.googleapis.com/css2?family=Open+Sans:wght@300;400;600;700&display=swap" rel="stylesheet">
<style>
  :root {
    --brand: #1f63ad;
    --brand-dark: #163f70;
    --panel-1: #1a4679;
    --panel-2: #1d5796;
    --panel-3: #2f80c8;
    --focus-bg: #1c4a80;
    --light: #fcfafc;
    --text: #444;
    --muted: #8a8a8a;
    --footer: #1d1d1d;
    --footer-base: #121212;
    --accent: #2a8fd6;
  }
  * { box-sizing: border-box; margin: 0; padding: 0; }
  html, body { width: 786px; height: 1200px; overflow: hidden; }
  body { font-family: "Open Sans", Arial, sans-serif; background: #fff; color: var(--text); position: relative; }

  .site-header { position: absolute; left: 0; top: 0; width: 786px; height: 80px; background: #fff; }
  .brand { position: absolute; left: 66px; top: 26px; display: flex; align-items: center; gap: 9px; }
  .brand-mark { width: 26px; height: 26px; background: var(--brand); }
  .brand-name { font-size: 19px; font-weight: 600; color: var(--brand); }
  .main-nav { position: absolute; right: 70px; top: 34px; display: flex; gap: 15px; font-size: 10.5px; color: #333; }

  .hero { position: absolute; left: 0; top: 80px; width: 786px; height: 313px;
    background: linear-gradient(180deg, #2467ae 0%, #1c5696 100%); }
  .hero-photo { position: absolute; left: 66px; top: 0; width: 444px; height: 313px;
    background: linear-gradient(135deg, #dfe7ee 0%, #a9bccd 55%, #4f7199 100%); }
  .cta-panel { position: absolute; left: 510px; top: 0; width: 203px; height: 313px; }
  .cta { position: absolute; left: 0; width: 203px; padding: 0 18px; color: #fff;
    font-size: 15px; font-weight: 300; line-height: 1.1; text-transform: uppercase; }
  .cta svg { display: block; margin-bottom: 6px; }
  .cta-newsletter { top: 0; height: 130px; background: var(--panel-1); padding-top: 30px; }
  .cta-clinic { top: 130px; height: 90px; background: var(--panel-2); padding-top: 14px; }
  .cta-intake { top: 220px; height: 93px; background: var(--panel-3); padding-top: 16px; }

  .focus { position: absolute; left: 0; top: 393px; width: 786px; height: 293px;
    background: linear-gradient(180deg, var(--focus-bg) 0%, #173f6e 100%); color: #fff; }
  .focus-title { position: absolute; top: 30px; width: 100%; text-align: center;
    font-size: 14px; font-weight: 400; letter-spacing: .5px; }
  .focus-item { position: absolute; top: 65px; width: 184px; }
  .focus-item:nth-of-type(1) { left: 86px; }
  .focus-item:nth-of-type(2) { left: 296px; }
  .focus-item:nth-of-type(3) { left: 506px; }
  .focus-image { width: 184px; height: 113px; }
  .focus-item h3 { font-size: 15px; font-weight: 400; margin: 13px 0 6px; }
  .focus-item p { font-size: 7px; line-height: 1.5; color: #d7e3f0; }

  .section-title { position: absolute; top: 764px; font-size: 14px; font-weight: 400; color: #333; text-transform: uppercase; }
  .testimonial { position: absolute; left: 86px; top: 795px; width: 334px; height: 96px;
    background: #f2f2f2; padding: 14px 16px 0 40px; }
  .testimonial .quote-mark { position: absolute; left: 12px; top: 4px; font-size: 38px; color: #bbb; line-height: 1; }
  .testimonial p { font-size: 7px; line-height: 1.55; color: var(--muted); font-style: normal; }
  .author { position: absolute; left: 100px; top: 905px; display: flex; align-items: center; gap: 10px; }
  .author-photo { width: 32px; height: 32px; border-radius: 50%; background: linear-gradient(135deg, #c9c9c9, #8f8f8f); }
  .author-name { font-size: 10px; color: #333; }
  .author-role { font-size: 7px; color: var(--muted); }
  .slider-dots { position: absolute; left: 374px; top: 922px; display: flex; gap: 5px; }
  .slider-dots span { width: 5px; height: 5px; border-radius: 50%; background: #c8c8c8; }
  .slider-dots span:first-child { background: #666; }
  .service-video { position: absolute; left: 453px; top: 792px; width: 249px; height: 146px; background: #111; }
  .service-video .frame { position: absolute; left: 0; top: 0; width: 249px; height: 130px;
    background: radial-gradient(circle at 60% 45%, #7a3a2a 0%, #2a1c22 45%, #0c0c14 100%); }
  .service-video .controls { position: absolute; left: 8px; bottom: 6px; width: 233px; height: 3px; background: #555; }
  .service-video .controls::before { content: ""; position: absolute; left: 0; top: 0; width: 40px; height: 3px; background: var(--accent); }

  .site-footer { position: absolute; left: 0; top: 975px; width: 786px; height: 225px; background: var(--footer); color: #9a9a9a; }
  .footer-col { position: absolute; top: 22px; font-size: 7.5px; line-height: 1.75; }
  .footer-col h4 { font-size: 8px; font-weight: 600; color: var(--accent); text-transform: uppercase; margin-bottom: 6px; letter-spacing: .3px; }
  .footer-col ul { list-style: none; }
  .col-sitemap { left: 66px; }
  .col-other { left: 210px; }
  .col-contact { left: 355px; }
  .col-social { left: 560px; width: 150px; }
  .social-row { display: flex; justify-content: space-between; align-items: center; height: 24px; }
  .social-dot { width: 15px; height: 15px; border-radius: 50%; background: var(--accent); }
  .footer-base { position: absolute; left: 0; bottom: 0; width: 786px; height: 47px; background: var(--footer-base);
    font-size: 7px; color: #777; text-align: center; line-height: 47px; }
</style>
</head>
<body>
  <header class="site-header">
    <div class="brand"><span class="brand-mark"></span><span class="brand-name">Het Zaakkompas</span></div>
    <nav class="main-nav">
      <span>Home</span><span>Who we are</span><span>How we work</span><span>Skills</span><span>Groeiateliers</span><span>Blog</span><span>Contact Us</span>
    </nav>
  </header>

  <section class="hero">
    <div class="hero-photo" role="img" aria-label="Photo of a smiling consultant with colleagues working in a bright office"></div>
    <div class="cta-panel">
      <div class="cta cta-newsletter">
        <svg width="20" height="16" viewBox="0 0 20 16"><rect x="1" y="1" width="18" height="14" fill="none" stroke="#fff" stroke-width="1.5"/><path d="M1 1 L10 9 L19 1" fill="none" stroke="#fff" stroke-width="1.5"/></svg>
        Register for<br>our newsletter
      </div>
      <div class="cta cta-clinic">
        <svg width="18" height="18" viewBox="0 0 18 18"><rect x="2" y="5" width="14" height="12" fill="#fff"/><path d="M6 5 V2 H12 V5" fill="none" stroke="#fff" stroke-width="1.5"/><path d="M9 8 V14 M6 11 H12" stroke="#1d5796" stroke-width="2"/></svg>
        Register for<br>a Groeiatelier
      </div>
      <div class="cta cta-intake">
        <svg width="20" height="18" viewBox="0 0 20 18"><path d="M2 2 H18 V12 H8 L4 16 V12 H2 Z" fill="none" stroke="#fff" stroke-width="1.5"/></svg>
        Ask a free<br>intake meeting
      </div>
    </div>
  </section>

  <section class="focus">
    <h2 class="focus-title">WE FOCUS ON</h2>
    <article class="focus-item">
      <div class="focus-image" role="img" aria-label="Image of a hand touching glowing marketing icons" style="background:linear-gradient(135deg,#2a2a3a,#8a5a3a 60%,#d08a3a)"></div>
      <h3>MARKETING</h3>
      <p>Sharp positioning, clear messages and campaigns that reach the right buyers. We help your team plan marketing that brings steady, measurable growth for your business.</p>
    </article>
    <article class="focus-item">
      <div class="focus-image" role="img" aria-label="Image of a sales chart with a pen on paper" style="background:linear-gradient(135deg,#1a2a44,#5c6f8c 55%,#c9d2de)"></div>
      <h3>SALES</h3>
      <p>From first contact to signed deal, we shape a sales approach that fits your company. Better follow-up, stronger pitches and more returning customers every single quarter.</p>
    </article>
    <article class="focus-item">
      <div class="focus-image" role="img" aria-label="Image of business technology and network devices" style="background:linear-gradient(135deg,#e8edf2,#b9c6d4 55%,#6f86a0)"></div>
      <h3>ICT</h3>
      <p>Smart tools and reliable systems that support daily work. We advise on software, security and the digital steps that make your small business faster and stronger.</p>
    </article>
  </section>

  <h2 class="section-title" style="left:86px">Testimonials</h2>
  <h2 class="section-title" style="left:453px">Our Services</h2>

  <blockquote class="testimonial">
    <span class="quote-mark">&ldquo;</span>
    <p>Working with this team gave our company a clear direction. Their advice on marketing and sales was practical, honest and easy to apply. Within months we saw more leads, better follow-up and a stronger position in our market. We can recommend them to every growing business.</p>
  </blockquote>
  <div class="author">
    <div class="author-photo" role="img" aria-label="Portrait of the client giving the testimonial"></div>
    <div><div class="author-name">Lukas Verbeke</div><div class="author-role">Company Name</div></div>
  </div>
  <div class="slider-dots"><span></span><span></span><span></span><span></span><span></span><span></span></div>

  <div class="service-video">
    <div class="frame" role="img" aria-label="Video still presenting the consultancy services"></div>
    <div class="controls"></div>
  </div>

  <footer class="site-footer">
    <div class="footer-col col-sitemap">
      <h4>Sitemap</h4>
      <ul><li>Home</li><li>Who we are</li><li>How we work</li><li>Skills</li><li>Groeiateliers</li><li>Blog</li><li>Contact Us</li></ul>
    </div>
    <div class="footer-col col-other">
      <h4>Other info</h4>
      <ul><li>Terms &amp; Conditions</li><li>Privacy Policy</li><li>Legal Notice</li></ul>
    </div>
    <div class="footer-col col-contact">
      <h4>Contact us</h4>
      <ul><li>Het Zaakkompas</li><li>Stationsstraat 12</li><li>9000 Gent</li><li>Belgium</li><li>&nbsp;</li><li>Telephone: +32 9 123 45 67</li><li>E-mail: info@zaakkompas.be</li></ul>
    </div>
    <div class="footer-col col-social">
      <h4>Connect with us</h4>
      <div class="social-row"><span>Facepage</span><span class="social-dot"></span></div>
      <div class="social-row"><span>Chirper</span><span class="social-dot"></span></div>
      <div class="social-row"><span>Linkwork</span><span class="social-dot"></span></div>
    </div>
    <div class="footer-base">&copy; 2015 Company Name | All Rights Reserved</div>
  </footer>
</body>
</html>
```